Business Card Design Project

I am looking for a classy business card design for a product design consultancy. We specialize in Product Design, Prototyping, and Manufacturing Consulting. Products that we design range from consumer electronics to household products all the way to sporting goods. We are based in Arizona and called "Heron Design Works." We like to have fun and goof off as much as we like to create new products. We are young and energetic so we would like our business cards to reflect that. We already have a logo that we would like to implement into the card design. A plain rectangular business card is boring so feel free to get creative, but please, no avocado shaped cards (it's far too literal). Also feel free to play around with textured card stocks or plastic. The final design that we choose will pay attention to all of the little details. Our cards will need to be 2 sided. We're giving you guys free reign to design as you would like. Please have fun with this, it will reflect in our business card.

Thanks guys,
Heron Design Works Team

Industry/Entity Type

Electronics

Requirements
Must have
• We would like to have a spot UV coating somewhere on the business card design if possible.
Nice to have
• Let's see some designs with custom shapes rather than typical rectangular business cards but please no avocado shaped cards, thanks. Also play around with textured card socks.

```html
<!DOCTYPE html>
<html lang="en">
<head>
<meta charset="utf-8">
<title>Heron Design Works — Business Card</title>
<link rel="stylesheet" href="https://fonts.googleapis.com/css2?family=Questrial&family=Arimo:wght@400&display=swap">
<style>
  :root {
    --card-brown: #2e261f;
    --leaf-green: #8cc63f;
    --stone-grey: #a9a9a9;
    --paper: #ffffff;
  }
  html, body {
    margin: 0;
    padding: 0;
    width: 1200px;
    height: 1000px;
    overflow: hidden;
    background: var(--paper);
  }
  .card-sheet { display: block; width: 1200px; height: 1000px; }
  .card-shape { fill: var(--card-brown); }
  .brand-dot { fill: var(--leaf-green); }
  .brand-name {
    font-family: "Questrial", sans-serif;
    font-size: 64px;
    fill: var(--leaf-green);
  }
  .person-name {
    font-family: "Arimo", sans-serif;
    font-size: 62px;
    fill: var(--leaf-green);
  }
  .person-role {
    font-family: "Arimo", sans-serif;
    font-size: 34px;
    fill: var(--stone-grey);
  }
  .contact-line {
    font-family: "Arimo", sans-serif;
    font-size: 30px;
    fill: var(--stone-grey);
  }
  .contact-key { fill: var(--leaf-green); }
</style>
</head>
<body>
<svg class="card-sheet" viewBox="0 0 1200 1000" xmlns="http://www.w3.org/2000/svg">

  <g class="card-front">
    <path class="card-shape" d="M125 35 H1045 A460 455 0 0 1 125 35 Z"/>
    <circle class="brand-dot" cx="258" cy="165" r="48"/>
    <text class="brand-name" x="330" y="187">Heron Design Works</text>
  </g>

  <g class="card-back">
    <path class="card-shape" d="M125 505 H1045 A460 455 0 0 1 125 505 Z"/>
    <text class="person-name" x="190" y="608">Marcus Hale</text>
    <text class="person-role" x="560" y="606">Creative Director</text>
    <circle class="brand-dot" cx="915" cy="625" r="52"/>

    <text class="contact-line" x="830" y="680" text-anchor="end"><tspan class="contact-key">w</tspan>: www.herondesign.com</text>
    <text class="contact-line" x="785" y="722" text-anchor="end"><tspan class="contact-key">e</tspan>: marcus@herondesign.com</text>
    <text class="contact-line" x="255" y="764"><tspan class="contact-key">f</tspan>: 555.014.229</text>
    <text class="contact-line" x="508" y="764"><tspan class="contact-key">c</tspan>: 555.014.229</text>
  </g>
</svg>
</body>
</html>
```